KVO - Redesign (PSD Files Only)

Requirements for the site:

1. We need our logo recreated, please use the same design and change colors to work on a white background

2. The site is a "Wizard" based site, that takes the customer through the process of creating a unique web presence that suits there needs

3.Colors Needed - Main "Dark Blue" Secondary = "Dark Grey" -Other = "Light Grey and White"

4.We need a CRISP CLEAN DESIGN, simple design

5.Wireframes are a general layout and may be modified by you to enhance the design

6. We want a complete web 5.0 look with big buttons and text boxes

7.The more personality the better

8. Current Site brightmorrowco.example

9.See attachments for wireframes

10. Designer should deliver PSD files, no coding is required

11. The portfolio wireframe, should look like the design of the pixelharbor portfolio template
Updates

KEEP IT SIMPLE.,.....

We like the quillframe scaffold style of designs

```html
<!DOCTYPE html>
<html lang="en">
<head>
<meta charset="utf-8">
<title>KVO – Custom Website Design</title>
<link href="https://fonts.googleapis.com/css2?family=Open+Sans:wght@400;600&family=Source+Sans+3:wght@400;600;700&display=swap" rel="stylesheet">
<style>
:root{
  --blue:#0f4fa0;
  --blue-band:#0d4f9e;
  --blue-soft:#a9c3e4;
  --dark:#3d3d3d;
  --dark-text:#333;
  --mid-text:#666;
  --muted:#9a9a9a;
  --light:#ebebeb;
  --white:#fff;
}
*{box-sizing:border-box;margin:0;padding:0}
html,body{width:1200px;height:1128px;overflow:hidden}
body{position:relative;background:var(--white);font-family:"Open Sans",sans-serif;color:var(--dark-text)}
.abs{position:absolute}

.topbar{left:0;top:0;width:1200px;height:35px;background:var(--dark)}
.nav a{position:absolute;top:9px;font-size:14px;color:#cfcfcf;text-decoration:none}
.social{top:8px}
.phone{right:198px;top:9px;font-size:14px;color:#cfcfcf}

.hero{left:0;top:35px;width:1200px;height:214px;background:var(--light);text-align:center}
.brand{position:absolute;left:0;width:1200px;top:38px;display:flex;justify-content:center;align-items:center;gap:8px}
.brand-mark{width:18px;height:18px;background:var(--blue)}
.brand-name{font-family:"Source Sans 3",sans-serif;font-weight:600;font-size:26px;color:var(--blue)}
.headline{position:absolute;width:1200px;top:92px;font-family:"Source Sans 3",sans-serif;font-weight:700;font-size:33px;letter-spacing:-1.2px;color:var(--blue)}
.subhead{position:absolute;width:1200px;top:134px;font-family:"Source Sans 3",sans-serif;font-weight:600;font-size:21px;letter-spacing:-.6px;color:var(--dark-text)}
.intro{position:absolute;left:340px;width:520px;top:161px;font-size:12.5px;line-height:15px;color:var(--mid-text)}

.feature{width:160px;text-align:center;font-family:"Source Sans 3",sans-serif;font-size:15px;line-height:18px;letter-spacing:-.5px;color:#555}
.feature svg{display:block;margin:0 auto 6px}

.step{left:0;width:1200px;top:412px;text-align:center;font-size:11px;color:#555}
.progress{left:520px;top:430px;width:161px;height:14px;background:var(--blue-soft)}
.progress span{display:block;width:37px;height:14px;background:var(--blue)}
.project-input{left:370px;top:465px;width:293px;height:36px;background:var(--light);border:1px solid #ccc;border-top:2px solid #bbb;font-size:12px;color:#999;padding:9px 9px}
.start-btn{left:671px;top:465px;width:159px;height:36px;background:var(--blue);color:var(--white);font-family:"Source Sans 3",sans-serif;font-weight:600;font-size:21px;letter-spacing:-.8px;text-align:center;line-height:35px}

.services{left:0;top:533px;width:1200px;height:272px;background:var(--light)}
.card{top:562px;width:187px;height:215px;background:var(--dark);padding:0 11px 0 11px}
.card-tab{position:absolute;left:-7px;top:7px;width:190px;height:30px;background:var(--white);clip-path:polygon(0 0,185px 0,190px 15px,185px 30px,0 30px);font-family:"Source Sans 3",sans-serif;font-weight:600;font-size:19px;letter-spacing:-.6px;color:var(--blue);padding-left:16px;line-height:30px}
.card p{margin-top:48px;font-size:11px;line-height:14px;color:#e8e8e8}
.card ul{margin-top:14px;list-style:none}
.card li{font-size:10px;line-height:15px;color:#a5a5a5;padding-left:10px;position:relative}
.card li::before{content:"•";position:absolute;left:0}

.portfolio{left:0;top:805px;width:1200px;height:272px;background:var(--blue-band)}
.shot{top:835px;width:193px;height:193px;border:4px solid #1b3560}
.dot{top:1039px;width:10px;height:10px;border-radius:50%;background:var(--white)}

.copyright{left:199px;top:1096px;font-size:11px;color:var(--muted)}
.copyright a{color:var(--dark-text);text-decoration:none}
.badge{left:912px;top:1085px;width:89px;height:33px;border:1px solid #ddd;background:#f6f6f6}
.badge span{position:absolute;left:0;top:0;width:31px;height:31px;background:#2d6cc0}
</style>
</head>
<body>

<header class="abs topbar">
  <nav class="nav">
    <a style="left:200px">Home</a>
    <a style="left:259px">About Us</a>
    <a style="left:338px">Portfolio</a>
    <a style="left:412px">Contact Us</a>
  </nav>
  <svg class="abs social" style="left:563px" width="72" height="20" aria-hidden="true">
    <circle cx="10" cy="10" r="9.5" fill="#888"/><circle cx="36" cy="10" r="9.5" fill="#888"/><circle cx="62" cy="10" r="9.5" fill="#888"/>
  </svg>
  <div class="abs phone">
    <svg width="11" height="12" viewBox="0 0 24 24" aria-hidden="true" style="vertical-align:-1px"><path fill="#cfcfcf" d="M6.6 10.8a15 15 0 0 0 6.6 6.6l2.2-2.2c.3-.3.7-.4 1-.2 1.1.4 2.3.6 3.6.6.6 0 1 .4 1 1V20c0 .6-.4 1-1 1A17 17 0 0 1 3 4c0-.6.4-1 1-1h3.5c.6 0 1 .4 1 1 0 1.3.2 2.5.6 3.6.1.3 0 .7-.2 1z"/></svg>1-800-555-0142
  </div>
</header>

<section class="abs hero">
  <div class="brand"><span class="brand-mark"></span><span class="brand-name">KVO Studios</span></div>
  <h1 class="headline">Get A Custom Website Design In 21 Days Or LESS!</h1>
  <h2 class="subhead">Find out why we’re the #1 custom website design marketplace.</h2>
  <p class="intro">Our network of designers will create 50+ web design samples for you to choose and our marketing experts will pave the way for your success.</p>
</section>

<div class="abs feature" style="left:243px;top:280px">
  <svg width="34" height="36" viewBox="0 0 34 36" aria-hidden="true"><circle cx="17" cy="17" r="15" fill="var(--blue)"/><circle cx="17" cy="19" r="9" fill="#fff"/><rect x="0" y="14" width="6" height="10" rx="2" fill="var(--blue)"/><rect x="28" y="14" width="6" height="10" rx="2" fill="var(--blue)"/></svg>
  24/7 Customer<br>Support
</div>
<div class="abs feature" style="left:423px;top:324px">
  <svg width="44" height="32" viewBox="0 0 44 32" aria-hidden="true"><ellipse cx="19" cy="13" rx="18" ry="12" fill="var(--blue)"/><ellipse cx="27" cy="18" rx="16" ry="11" fill="var(--blue)"/><path d="M34 26l6 6-10-3z" fill="var(--blue)"/><text x="14" y="18" font-size="14" font-weight="700" fill="#fff" font-family="sans-serif">”</text></svg>
  100% No Obligation<br>Free Web Quote
</div>
<div class="abs feature" style="left:617px;top:324px">
  <svg width="36" height="32" viewBox="0 0 36 32" aria-hidden="true"><path d="M3 6h9v3H6v17h24V9h-6V6h9v23H3z" fill="var(--blue)"/><path d="M15 2h6v10h5l-8 9-8-9h5z" fill="var(--blue)"/></svg>
  Save 1000’s On<br>Web Design
</div>
<div class="abs feature" style="left:790px;top:280px">
  <svg width="34" height="36" viewBox="0 0 34 36" aria-hidden="true"><rect x="0" y="15" width="8" height="19" fill="var(--blue)"/><path d="M10 16l7-12c2-3 5-2 5 1l-1 9h10c2 0 3 2 2 4l-4 14c-1 2-2 2-3 2H10z" fill="var(--blue)"/></svg>
  100% Moneyback<br>Gaurantee
</div>

<svg class="abs" style="left:300px;top:365px" width="160" height="130" aria-hidden="true">
  <path d="M153 14C110-5 30-5 12 50c-12 38 20 65 46 68" fill="none" stroke="#888" stroke-width="1" stroke-dasharray="3 3"/>
  <path d="M52 110l7 8-9 4" fill="none" stroke="#888" stroke-width="1"/>
</svg>

<div class="abs step">Step 1</div>
<div class="abs progress"><span></span></div>
<div class="abs project-input">Name Your Project...</div>
<div class="abs start-btn">Start Your Project</div>

<section class="abs services"></section>
<article class="abs card" style="left:207px">
  <div class="card-tab">Why Choose KVO?</div>
  <p>We are a full service design &amp; marketingcompany tha will handle everything.</p>
  <ul><li>Dedicated Project</li><li>Manager</li><li>Single Point Contact</li><li>Low Cost</li><li>50+ Design Samples for you to choose.</li></ul>
</article>
<article class="abs card" style="left:409px">
  <div class="card-tab">Web Services</div>
  <p>We specialize in the following design services:</p>
  <ul><li>Web Design</li><li>Ecommerce Design</li><li>Web Programming</li><li>Logo Design</li><li>Stationary/Print Design</li><li>Ad Design</li><li>Email Template Design.</li></ul>
</article>
<article class="abs card" style="left:612px">
  <div class="card-tab">Marketing Services</div>
  <p>We handle all online marketing including the following:</p>
  <ul><li>Paid Search Ads</li><li>Local Map Marketing</li><li>Search Engine Optimization</li><li>Email Marketing</li><li>Social Media Marketing.</li></ul>
</article>
<article class="abs card" style="left:814px">
  <div class="card-tab">Maintainence Services</div>
  <p>Let us maintain your site and save up to 50% on the following:</p>
  <ul><li>Website Hosting</li><li>Software Upgrades</li><li>Custom Web Programming</li><li>Website Marketing</li></ul>
</article>

<section class="abs portfolio"></section>
<svg class="abs" style="left:176px;top:903px" width="16" height="56" aria-hidden="true"><path d="M14 2L3 28l11 26" fill="none" stroke="#cfe0f5" stroke-width="1.5"/></svg>
<svg class="abs" style="left:1008px;top:903px" width="16" height="56" aria-hidden="true"><path d="M2 2l11 26L2 54" fill="none" stroke="#cfe0f5" stroke-width="1.5"/></svg>
<div class="abs shot" style="left:200px;background:linear-gradient(135deg,#a8752e,#d9a55a 50%,#7a4a1e)" role="img" aria-label="Portfolio sample: restaurant website with food photography"></div>
<div class="abs shot" style="left:404px;background:linear-gradient(180deg,#fafafa 0,#f1ece6 55%,#ffffff 56%)" role="img" aria-label="Portfolio sample: cafe website with menu highlights"></div>
<div class="abs shot" style="left:606px;background:linear-gradient(180deg,#1a3f9a 0,#3b79d6 35%,#9fc7ee 60%,#fff 78%)" role="img" aria-label="Portfolio sample: pressure washing company website with city skyline"></div>
<div class="abs shot" style="left:808px;background:linear-gradient(160deg,#ffffff 0,#d8ecfb 40%,#63aee8 70%,#9bc86a)" role="img" aria-label="Portfolio sample: garden center website with flowers"></div>
<div class="abs dot" style="left:572px"></div>
<div class="abs dot" style="left:587px"></div>
<div class="abs dot" style="left:603px"></div>
<div class="abs dot" style="left:618px"></div>

<footer>
  <div class="abs copyright">Copyright © 2014 KVO Studios. All Right Reserved &nbsp;|&nbsp; <a>Request Consultation</a></div>
  <div class="abs badge" role="img" aria-label="Partner badge"><span></span></div>
</footer>

</body>
</html>
```